Flyer-Design für renomiertes Kosmetikstudio
Zielgruppe
Renomiertes Kosmetikstudio sucht hochwertiges Design für neue Flyer.
Zielgruppe Männer + Frauen die auf ihr Äußeres viel Wert legen.
Aufgabenstellung
Geradliniges Desgin unter Berücksichtigung von ganzheitlichen Farben (chakren). Edel.
Wir hätten gerne ein Angebot für Männer als auch für Frauen. Evtl. Aufteilung in 2 getrennte Flyer oder Flyer auf einer Seite Männer und umgedreht auf der anderen Seite für Frauen.?
Behandlungsbereiche die aufgenommen werden müssten:
Frauen
- Wimpernverlängerung
- Wimpernlifting
- Kosmetikbehandlung (Fresh Start - Encore Konzept) ausführlicher text dazu
zzgl. möglichen Bausteinen
- Fußpflege
- Nageldesign
- Enthaarung mit Zuckerpaste
- Massagen
Männer:
- Kosmetikbehandlung
- Maniküre
-- Massage
- Enthaarung
Für die Kosmetik hätte ich gerne jeweils 1 Seite komplett um hier mehr Infos rein zu packen zur FRESH START Behandlung.
Platz für Preise der Behandlungen und bausteine.
Gewünscht Din Lang Format, gerne aber auch offen für neue Ideen.

```html
<!DOCTYPE html>
<html lang="de">
<head>
<meta charset="utf-8">
<title>Lumera – Preisliste und Angebote für Männer</title>
<link href="https://fonts.googleapis.com/css2?family=Open+Sans:ital,wght@0,300;0,400;0,600;0,700;1,400;1,700&family=Raleway:wght@300;400&display=swap" rel="stylesheet">
<style>
:root{
  --pink:#e05a9b;
  --cyan:#5cc4dc;
  --taupe:#b7adae;
  --ink:#4a4a4a;
  --soft:#8a8a8a;
  --line:#9c9c9c;
  --row:#ececec;
  --paper:#ffffff;
  --stage:#ececec;
}
*{box-sizing:border-box;margin:0;padding:0}
html,body{width:1200px;height:2667px;overflow:hidden;background:var(--stage)}
body{position:relative;font-family:"Open Sans",sans-serif;color:var(--ink)}
.sheet{position:absolute;background:var(--paper);overflow:hidden;box-shadow:0 6px 22px rgba(0,0,0,.12)}
.trifold{left:150px;width:900px;height:630px;display:flex}
.trifold.outside{top:90px}
.trifold.inside{top:930px}
.panel{position:relative;width:300px;height:630px;overflow:hidden;border-right:1px solid #e2e2e2}
.panel:last-child{border-right:0}
.theme-pink{--accent:var(--pink)}
.theme-cyan{--accent:var(--cyan)}
.photo{position:absolute}
.wave{position:absolute;left:0;width:100%;display:block}
.section-title{color:var(--accent);font-weight:700;font-size:13px}
.intro{font-size:6.5px;line-height:1.45;color:var(--soft);margin-top:4px}
.price-box{position:relative;border:1.4px solid var(--line);border-radius:6px;padding:11px 6px 5px;margin-top:16px;background:#fff}
.price-box .tab{position:absolute;top:-8px;left:50%;transform:translateX(-50%);background:var(--taupe);color:#fff;border-radius:8px;padding:0 9px;font-size:8px;line-height:14px;white-space:nowrap}
.row{display:flex;align-items:center;font-size:6.5px;height:11px;color:var(--ink)}
.row:nth-child(odd){background:var(--row)}
.row .name{flex:1;padding-left:3px;white-space:nowrap;overflow:hidden}
.row .time{width:46px;border-left:1px solid var(--line);display:flex;align-items:center;gap:3px;padding-left:4px}
.row .price{width:46px;border-left:1px solid var(--line);display:flex;align-items:center;justify-content:space-between;padding:0 3px 0 4px}
.ico{width:7px;height:7px;color:var(--accent);flex:none}
.eur{display:inline-flex;align-items:center;justify-content:center;width:7px;height:7px;border:0.8px solid var(--accent);border-radius:50%;color:var(--accent);font-size:4.5px;line-height:1}
.wordmark{font-family:"Open Sans",sans-serif;font-weight:600;letter-spacing:0;color:var(--ink)}
.tagline{font-size:6px;color:var(--soft)}
.url-pill{display:inline-block;background:var(--accent);color:#fff;border-radius:9px;padding:0 10px;font-size:9px;line-height:17px}
.url-pill.dark{background:#5d5d5d}
.badge{position:absolute;background:var(--accent);border:2px solid #fff;outline:2px solid var(--accent);border-radius:14px 4px 14px 4px;color:#fff;text-align:center;letter-spacing:.12em}
.badge svg{display:block;margin:0 auto}

.care{padding:18px 16px 0}
.care .block+.block{margin-top:18px}
.welcome-banner{position:absolute;top:14px;left:40px;background:var(--pink);color:#fff;font-size:8px;padding:2px 10px;border-radius:2px;transform:rotate(-4deg)}
.team{position:absolute;left:148px;top:70px;width:100px;height:80px;border:3px solid var(--pink);border-radius:10px;background:linear-gradient(135deg,#3a2e30,#c9a598 55%,#2d2426)}
.contact-band{position:absolute;top:150px;left:0;width:100%;height:250px;background:var(--taupe)}
.contact-band .brand{position:absolute;left:20px;top:40px}
.contact-band .brand .wordmark{color:#fff;font-size:17px}
.contact-band .brand .tagline{color:#fff}
.contact-cols{position:absolute;left:20px;top:100px;right:14px;display:flex;gap:16px;color:#fff;font-size:6px;line-height:1.6}
.contact-cols h4{font-size:6.5px;font-weight:600;margin-bottom:3px}
.social{position:absolute;left:22px;top:200px;display:flex;gap:8px}
.social span{width:15px;height:15px;background:var(--pink);border-radius:2px}
.cover-brand{position:absolute;top:24px;left:0;width:100%;text-align:center}
.cover-brand .wordmark{font-size:19px}
.cover-band{position:absolute;left:0;bottom:0;width:100%;height:210px;background:var(--taupe);text-align:center;color:#fff}
.cover-band h2{font-family:"Raleway",sans-serif;font-weight:400;font-size:28px;letter-spacing:.14em;margin-top:40px}
.cover-band .sub{display:flex;align-items:center;justify-content:center;gap:8px;font-size:9px;margin-top:4px}
.cover-band .sub i{display:block;width:40px;height:1px;background:#fff}
.cover-band .url-pill{margin-top:14px}

.lashes{padding:20px 16px 0}
.lashes .block+.block{margin-top:20px}
.treatment{position:absolute;top:160px;left:0;width:100%;padding:0 16px}
.concept-tab{display:block;width:fit-content;margin:8px auto 4px;background:var(--taupe);color:#fff;font-style:italic;font-size:8px;padding:1px 12px;border-radius:8px}
.treatment p{font-size:6.5px;line-height:1.5;color:var(--soft);margin-top:6px}
.sugar{padding:20px 16px 0}
.sugar .block+.block{margin-top:20px}

.men{top:1742px;width:409px;height:815px}
.men.front{left:151px}
.men.back{left:660px}
.top-bar{position:absolute;top:0;left:0;width:100%;height:9px;background:var(--cyan)}
.men-brand{position:absolute;top:36px;left:0;width:100%;text-align:center}
.men-brand .wordmark{font-size:31px}
.men-brand .tagline{font-size:13px;margin-top:2px}
.men-band{position:absolute;left:0;bottom:0;width:100%;height:185px;background:var(--taupe);text-align:center;color:#fff}
.men-band h2{font-family:"Raleway",sans-serif;font-weight:400;font-size:44px;letter-spacing:.1em;margin-top:52px}
.men-band .sub{display:flex;align-items:center;justify-content:center;gap:10px;font-size:15px}
.men-band .sub i{display:block;width:62px;height:1.5px;background:#fff}
.men-band .url-pill{font-size:15px;line-height:25px;padding:0 14px;border-radius:12px;margin-top:16px}
.men-back-body{position:absolute;top:30px;left:33px;right:33px}
.men-back-body h1{display:inline-block;color:var(--cyan);font-weight:700;font-size:21px;padding:0 6px 8px 0;border-bottom:1px solid #bbb;white-space:nowrap}
.men-back-body .intro{font-size:9.5px;line-height:1.2;margin-top:14px;color:var(--soft)}
.men .price-box{margin-top:26px;padding:12px 6px 4px;border-width:1.6px;border-color:#666}
.men .price-box .tab{font-size:13px;line-height:20px;top:-11px;border-radius:10px}
.men .row{font-size:9.5px;height:21px}
.men .row .time,.men .row .price{width:80px}
.men .ico{width:11px;height:11px}
.men .eur{width:11px;height:11px;font-size:7px}
.men-contact{position:absolute;left:0;bottom:0;width:100%;height:104px;background:var(--taupe);color:#fff;padding:14px 34px;font-size:9.5px;line-height:1.55}
.men-contact h4{font-size:10.5px;font-weight:600;margin-bottom:6px}
.men-contact .line{display:flex;align-items:center;gap:6px}
.men-contact .line b{font-weight:400;width:46px}
</style>
</head>
<body>

<svg width="0" height="0" style="position:absolute" aria-hidden="true">
  <defs>
    <symbol id="clock" viewBox="0 0 12 12"><circle cx="6" cy="6" r="5" fill="none" stroke="currentColor" stroke-width="1.2"/><path d="M6 3v3.2l2 1.3" fill="none" stroke="currentColor" stroke-width="1.2" stroke-linecap="round"/></symbol>
    <symbol id="phone" viewBox="0 0 24 24"><path d="M6.6 2.5l3 .4 1.2 4.3-2 1.6c1 2.2 2.6 3.8 4.7 4.9l1.6-2 4.3 1.2.4 3c0 1-.8 1.8-1.8 1.8C10.4 17.7 4.3 11.6 4.3 4.3c0-1 .8-1.8 2.3-1.8z" fill="none" stroke="currentColor" stroke-width="1.8" stroke-linejoin="round"/></symbol>
    <symbol id="calendar" viewBox="0 0 24 24"><rect x="3" y="5" width="18" height="16" rx="2" fill="none" stroke="currentColor" stroke-width="1.8"/><path d="M3 9h18M8 3v4M16 3v4M8.5 15l2.5 2.5 4.5-5" fill="none" stroke="currentColor" stroke-width="1.8" stroke-linecap="round"/></symbol>
    <symbol id="pin" viewBox="0 0 12 12"><path d="M6 11S2 7 2 4.5a4 4 0 018 0C10 7 6 11 6 11z" fill="currentColor"/><circle cx="6" cy="4.5" r="1.4" fill="#b7adae"/></symbol>
    <symbol id="mail" viewBox="0 0 12 12"><rect x="1" y="2.5" width="10" height="7" fill="currentColor"/><path d="M1 2.5l5 4 5-4" fill="none" stroke="#b7adae" stroke-width="1"/></symbol>
  </defs>
</svg>

<!-- Trifold outside -->
<section class="sheet trifold outside theme-pink">
  <div class="panel care">
    <div class="block">
      <h3 class="section-title">Fußpflege</h3>
      <p class="intro">Klassische Fußpflege mit Fußbad, auf Wunsch gerne auch mit Lack oder dauerhaftem Nagellack, Zehenschutz und Fußmassage inklusive.</p>
      <div class="price-box"><span class="tab">Fußpflege</span>
        <div class="row"><span class="name">Klassische Fußpflege inkl. Fußbad</span><span class="time"><svg class="ico"><use href="#clock"/></svg>60 min.</span><span class="price"><span class="eur">€</span>38,00</span></div>
        <div class="row"><span class="name">Fußpflege mit dauerhaftem Lack</span><span class="time"><svg class="ico"><use href="#clock"/></svg>75 min.</span><span class="price"><span class="eur">€</span>52,00</span></div>
        <div class="row"><span class="name">Zusatz: Klarlack</span><span class="time"><svg class="ico"><use href="#clock"/></svg>5 min.</span><span class="price"><span class="eur">€</span>3,00</span></div>
        <div class="row"><span class="name">Zusatz: Farblack</span><span class="time"><svg class="ico"><use href="#clock"/></svg>10 min.</span><span class="price"><span class="eur">€</span>5,00</span></div>
        <div class="row"><span class="name">Fußpeeling</span><span class="time"><svg class="ico"><use href="#clock"/></svg>5 min.</span><span class="price"><span class="eur">€</span>5,00</span></div>
        <div class="row"><span class="name">Kleine Fußmassage</span><span class="time"><svg class="ico"><use href="#clock"/></svg>10 min.</span><span class="price"><span class="eur">€</span>12,00</span></div>
        <div class="row"><span class="name">Ablackieren</span><span class="time"><svg class="ico"><use href="#clock"/></svg>5 min.</span><span class="price"><span class="eur">€</span>4,00</span></div>
        <div class="row"><span class="name">French</span><span class="time"><svg class="ico"><use href="#clock"/></svg>5 min.</span><span class="price"><span class="eur">€</span>5,00</span></div>
      </div>
    </div>
    <div class="block">
      <h3 class="section-title">Nageldesign</h3>
      <p class="intro">Gepflegte Hände sind täglich unsere Visitenkarte. Von der klassischen Maniküre bis hin zur Nagelmodellage finden Sie garantiert die passende Behandlung.</p>
      <div class="price-box"><span class="tab">Nageldesign</span>
        <div class="row"><span class="name">Maniküre</span><span class="time"><svg class="ico"><use href="#clock"/></svg>20 min.</span><span class="price"><span class="eur">€</span>17,00</span></div>
        <div class="row"><span class="name">Dauerhafter Nagellack</span><span class="time"><svg class="ico"><use href="#clock"/></svg>45 min.</span><span class="price"><span class="eur">€</span>29,00</span></div>
        <div class="row"><span class="name">Gelmodellage mit neu Verlängerung</span><span class="time"><svg class="ico"><use href="#clock"/></svg>90 min.</span><span class="price"><span class="eur">€</span>46,50</span></div>
        <div class="row"><span class="name">Gelmodellage auffüllen</span><span class="time"><svg class="ico"><use href="#clock"/></svg>75 min.</span><span class="price"><span class="eur">€</span>39,50</span></div>
        <div class="row"><span class="name">Naturnagelverstärkung</span><span class="time"><svg class="ico"><use href="#clock"/></svg>60 min.</span><span class="price"><span class="eur">€</span>20,00</span></div>
        <div class="row"><span class="name">Fresh up</span><span class="time"><svg class="ico"><use href="#clock"/></svg>45 min.</span><span class="price"><span class="eur">€</span>35,00</span></div>
        <div class="row"><span class="name">Wellnessmaniküre</span><span class="time"><svg class="ico"><use href="#clock"/></svg>35 min.</span><span class="price"><span class="eur">€</span>29,00</span></div>
      </div>
    </div>
    <div class="photo" role="img" aria-label="Foto: Maniküre an einer Hand mit Nagelfeile" style="left:0;bottom:0;width:300px;height:120px;background:linear-gradient(160deg,#f3e7e1,#e8cfc4 50%,#f6f1ee)"></div>
    <svg class="wave" style="bottom:90px" viewBox="0 0 300 40" height="40" preserveAspectRatio="none"><path d="M0 0V24C60 6 120 38 190 22 240 10 270 4 300 2V0Z" fill="#fff"/><path d="M0 26C60 8 120 40 190 24 240 12 270 6 300 4" fill="none" stroke="var(--pink)" stroke-width="4"/></svg>
  </div>

  <div class="panel">
    <div class="photo" role="img" aria-label="Foto: heller Empfangsbereich des Studios" style="left:0;top:0;width:300px;height:170px;background:linear-gradient(135deg,#c9a57a,#efe4d4 55%,#a67f55)"></div>
    <span class="welcome-banner">Wir freuen uns auf Ihren Besuch!</span>
    <div class="contact-band">
      <svg class="wave" style="top:-18px" viewBox="0 0 300 30" height="30" preserveAspectRatio="none"><path d="M0 30V14C50 2 90 26 150 14 210 2 250 22 300 10V30Z" fill="var(--taupe)"/></svg>
      <div class="brand"><div class="wordmark">Lumera</div><div class="tagline">Studio für Kosmetik und Pflege</div></div>
      <div class="contact-cols">
        <div><h4>Kontakt</h4>Lindenweg 14<br>20457 Hafenstadt<br><br>04120 55 38 210<br>info@lumera-studio.de<br>studio-lumera.de</div>
        <div><h4>Öffnungszeiten</h4>Mo, Di, Fr: 8:30 – 17:00 Uhr<br>Mittwoch: 8:30 – 14:00 Uhr<br>Donnerstag: 8:30 – 19:00 Uhr<br><br>Samstag und Abendtermine<br>nach Vereinbarung</div>
      </div>
      <div class="social"><span></span><span></span><span></span></div>
      <svg class="wave" style="bottom:-16px" viewBox="0 0 300 30" height="30" preserveAspectRatio="none"><path d="M0 0V16C50 30 100 8 160 18 220 28 260 10 300 14V0Z" fill="var(--taupe)"/><path d="M0 16C50 30 100 8 160 18 220 28 260 10 300 14" fill="none" stroke="#5d5d5d" stroke-width="3"/></svg>
    </div>
    <div class="team" role="img" aria-label="Foto: das Team des Studios"></div>
    <div class="photo" role="img" aria-label="Foto: Behandlungsraum mit Holzmöbeln" style="left:0;top:415px;width:300px;height:215px;background:linear-gradient(135deg,#b48a5a,#f1e6d6 50%,#c7a47a)"></div>
    <div class="badge" style="left:170px;top:360px;width:96px;height:76px;padding-top:8px;font-size:9px;line-height:1.2">
      <svg width="14" height="14" style="color:#fff"><use href="#calendar"/></svg>TERMINE<br>ONLINE<br>BUCHEN!
    </div>
    <div style="position:absolute;left:0;bottom:12px;width:100%;text-align:center"><span class="url-pill">www.lumera-studio.de</span></div>
  </div>

  <div class="panel">
    <div class="photo" role="img" aria-label="Foto: lächelnde Frau mit gepflegter Haut" style="left:0;top:80px;width:300px;height:360px;background:linear-gradient(160deg,#f4efee,#e9cfc2 45%,#d8c8c4)"></div>
    <svg class="wave" style="top:70px" viewBox="0 0 300 40" height="40" preserveAspectRatio="none"><path d="M0 0V30C60 8 110 36 170 20 230 6 270 16 300 10V0Z" fill="#fff"/><path d="M0 30C60 8 110 36 170 20 230 6 270 16 300 10" fill="none" stroke="#5d5d5d" stroke-width="3"/></svg>
    <div class="cover-brand"><div class="wordmark">Lumera</div><div class="tagline">Studio für Kosmetik und Pflege</div></div>
    <div class="badge" style="left:170px;top:250px;width:100px;height:80px;padding-top:8px;font-size:8px;line-height:1.2">
      <svg width="14" height="14" style="color:#fff"><use href="#phone"/></svg>TERMINE:<br><span style="font-size:12px;letter-spacing:.02em">04120<br>55 38 210</span>
    </div>
    <div class="cover-band">
      <svg class="wave" style="top:-16px" viewBox="0 0 300 30" height="30" preserveAspectRatio="none"><path d="M0 30V12C70 30 120 0 190 14 240 24 270 10 300 6V30Z" fill="var(--taupe)"/></svg>
      <h2>PREISLISTE</h2>
      <div class="sub"><i></i>für 2019<i></i></div>
      <span class="url-pill dark">www.lumera-studio.de</span>
    </div>
  </div>
</section>

<!-- Trifold inside -->
<section class="sheet trifold inside theme-pink">
  <div class="panel lashes">
    <div class="block">
      <h3 class="section-title">Wimpernverlängerung</h3>
      <p class="intro">Mit einer professionellen Wimpernverlängerung oder Wimpernverdichtung der Velisse-Linie gehört Wimperntusche der Vergangenheit an.</p>
      <div class="price-box"><span class="tab">Wimpernverlängerung</span>
        <div class="row"><span class="name">Neuaufbau</span><span class="time"><svg class="ico"><use href="#clock"/></svg>90 min.</span><span class="price"><span class="eur">€</span>190,00</span></div>
        <div class="row"><span class="name">Neuaufbau Volumentechnik</span><span class="time"><svg class="ico"><use href="#clock"/></svg>90 min.</span><span class="price"><span class="eur">€</span>280,00</span></div>
        <div class="row"><span class="name">Refill nach 2 Wochen</span><span class="time"><svg class="ico"><use href="#clock"/></svg>45 min.</span><span class="price"><span class="eur">€</span>45,00</span></div>
        <div class="row"><span class="name">Refill nach 3 Wochen</span><span class="time"><svg class="ico"><use href="#clock"/></svg>60 min.</span><span class="price"><span class="eur">€</span>52,00</span></div>
        <div class="row"><span class="name">Refill nach 4 Wochen</span><span class="time"><svg class="ico"><use href="#clock"/></svg>60 min.</span><span class="price"><span class="eur">€</span>68,00</span></div>
        <div class="row"><span class="name">Wimpernverlängerung entfernen</span><span class="time"><svg class="ico"><use href="#clock"/></svg>30 min.</span><span class="price"><span class="eur">€</span>25,00</span></div>
        <div class="row"><span class="name">Refill Volumentechnik</span><span class="time"><svg class="ico"><use href="#clock"/></svg>10 min.</span><span class="price"><span class="eur">€</span>+15,00</span></div>
      </div>
    </div>
    <div class="block">
      <h3 class="section-title">Wimpernlifting</h3>
      <p class="intro">Mit einem professionellen Wimpernlifting der Velisse-Linie erhalten Ihre Naturwimpern einen sanften, langanhaltenden Schwung.</p>
      <div class="price-box"><span class="tab">Wimpernlifting</span>
        <div class="row"><span class="name">Neuaufbau</span><span class="time"><svg class="ico"><use href="#clock"/></svg>90 min.</span><span class="price"><span class="eur">€</span>190,00</span></div>
        <div class="row"><span class="name">Neuaufbau Volumentechnik</span><span class="time"><svg class="ico"><use href="#clock"/></svg>90 min.</span><span class="price"><span class="eur">€</span>280,00</span></div>
        <div class="row"><span class="name">Refill nach 2 Wochen</span><span class="time"><svg class="ico"><use href="#clock"/></svg>45 min.</span><span class="price"><span class="eur">€</span>45,00</span></div>
      </div>
    </div>
    <div class="photo" role="img" aria-label="Foto: Augenpartie mit langen Wimpern" style="left:0;bottom:0;width:300px;height:180px;background:linear-gradient(160deg,#f3e6e0,#e4c9bd 50%,#efe4e0)"></div>
    <svg class="wave" style="bottom:150px" viewBox="0 0 300 40" height="40" preserveAspectRatio="none"><path d="M0 0V20C50 2 100 8 150 22 210 38 260 30 300 36V0Z" fill="#fff"/><path d="M0 20C50 2 100 8 150 22 210 38 260 30 300 36" fill="none" stroke="var(--pink)" stroke-width="4"/></svg>
  </div>

  <div class="panel">
    <div class="photo" role="img" aria-label="Foto: Behandlungsliege in hellem Kosmetikraum" style="left:0;top:0;width:300px;height:160px;background:linear-gradient(135deg,#e9e6e3,#fafaf9 45%,#8c7e77)"></div>
    <svg class="wave" style="top:130px" viewBox="0 0 300 40" height="40" preserveAspectRatio="none"><path d="M0 40V18C60 38 120 4 180 16 230 26 270 12 300 8V40Z" fill="#fff"/><path d="M0 18C60 38 120 4 180 16 230 26 270 12 300 8" fill="none" stroke="var(--pink)" stroke-width="4"/></svg>
    <div class="treatment">
      <h3 class="section-title" style="margin-top:14px">Kosmetikbehandlungen</h3>
      <span class="concept-tab">Fresh Start - Encore Konzept</span>
      <p>Lorem ipsum dolor sit amet, consetetur sadipscing elitr, sed diam nonumy eirmod tempor invidunt ut labore et dolore magna aliquyam erat, sed diam voluptua. At vero eos et accusam et justo duo dolores et ea rebum. Stet clita kasd gubergren, no sea takimata sanctus est lorem ipsum dolor sit amet.</p>
      <p>Lorem ipsum dolor sit amet, consetetur sadipscing elitr, sed diam nonumy eirmod tempor invidunt ut labore et dolore magna aliquyam erat, sed diam voluptua. At vero eos et accusam et justo duo dolores et ea rebum. Stet clita kasd gubergren, no sea takimata sanctus est lorem ipsum dolor sit amet. Lorem ipsum dolor sit amet, consetetur sadipscing elitr.</p>
      <p>Lorem ipsum dolor sit amet, consetetur sadipscing elitr, sed diam nonumy eirmod tempor invidunt ut labore et dolore magna aliquyam erat. At vero eos et accusam et justo duo dolores et ea rebum.</p>
      <div class="price-box"><span class="tab" style="font-style:italic">Fresh Start - Encore</span>
        <div class="row"><span class="name">Lorem ipsum dolor</span><span class="time"><svg class="ico"><use href="#clock"/></svg>90 min.</span><span class="price"><span class="eur">€</span>190,00</span></div>
        <div class="row"><span class="name">Lorem ipsum dolor</span><span class="time"><svg class="ico"><use href="#clock"/></svg>90 min.</span><span class="price"><span class="eur">€</span>280,00</span></div>
        <div class="row"><span class="name">Lorem ipsum dolor</span><span class="time"><svg class="ico"><use href="#clock"/></svg>45 min.</span><span class="price"><span class="eur">€</span>45,00</span></div>
      </div>
      <p>Lorem ipsum dolor sit amet, consetetur sadipscing elitr, sed diam nonumy eirmod tempor invidunt ut labore et dolore magna aliquyam erat, sed diam voluptua.</p>
    </div>
  </div>

  <div class="panel sugar">
    <div class="block">
      <h3 class="section-title">Enthaarung mit Zuckerpaste</h3>
      <p class="intro">Lorem ipsum dolor sit amet, consetetur sadipscing elitr, sed diam nonumy eirmod tempor invidunt ut labore et dolore magna aliquyam erat, sed diam voluptua. At vero eos et accusam et justo duo dolores et ea rebum.</p>
      <div class="price-box"><span class="tab">Enthaarung</span>
        <div class="row"><span class="name">Beratungsgespräch Sugaring + Nuvella</span><span class="time"><svg class="ico"><use href="#clock"/></svg>15 min.</span><span class="price"><span class="eur">€</span>25,00</span></div>
        <div class="row"><span class="name">Unterschenkel inkl. Knie</span><span class="time"><svg class="ico"><use href="#clock"/></svg>30 min.</span><span class="price"><span class="eur">€</span>49,00</span></div>
        <div class="row"><span class="name">Beine komplett</span><span class="time"><svg class="ico"><use href="#clock"/></svg>60 min.</span><span class="price"><span class="eur">€</span>95,00</span></div>
        <div class="row"><span class="name">Arme komplett</span><span class="time"><svg class="ico"><use href="#clock"/></svg>30 min.</span><span class="price"><span class="eur">€</span>45,00</span></div>
        <div class="row"><span class="name">Achseln</span><span class="time"><svg class="ico"><use href="#clock"/></svg>15 min.</span><span class="price"><span class="eur">€</span>34,00</span></div>
        <div class="row"><span class="name">Teile Gesicht</span><span class="time"><svg class="ico"><use href="#clock"/></svg>10 min.</span><span class="price"><span class="eur">€</span>15,00</span></div>
        <div class="row"><span class="name">Bikinizone</span><span class="time"><svg class="ico"><use href="#clock"/></svg>20 min.</span><span class="price"><span class="eur">€</span>42,00</span></div>
        <div class="row"><span class="name">Nasen- und Ohrenhaare</span><span class="time"><svg class="ico"><use href="#clock"/></svg>10 min.</span><span class="price"><span class="eur">€</span>10,00</span></div>
        <div class="row"><span class="name">Rücken</span><span class="time"><svg class="ico"><use href="#clock"/></svg>30 min.</span><span class="price"><span class="eur">€</span>74,00</span></div>
        <div class="row"><span class="name">Intim (nur für Damen)</span><span class="time"><svg class="ico"><use href="#clock"/></svg>45 min.</span><span class="price"><span class="eur">€</span>68,00</span></div>
        <div class="row"><span class="name">Bauch</span><span class="time"><svg class="ico"><use href="#clock"/></svg>20 min.</span><span class="price"><span class="eur">€</span>45,00</span></div>
        <div class="row"><span class="name">Brust</span><span class="time"><svg class="ico"><use href="#clock"/></svg>20 min.</span><span class="price"><span class="eur">€</span>45,00</span></div>
        <div class="row"><span class="name">Lorem ipsum Dolor</span><span class="time"><svg class="ico"><use href="#clock"/></svg>10 min.</span><span class="price"><span class="eur">€</span>14,00</span></div>
        <div class="row"><span class="name">Lorem ipsum Dolor</span><span class="time"><svg class="ico"><use href="#clock"/></svg>20 min.</span><span class="price"><span class="eur">€</span>45,00</span></div>
      </div>
    </div>
    <div class="block">
      <h3 class="section-title">Massagen</h3>
      <p class="intro">Lorem ipsum dolor sit amet, consetetur sadipscing elitr, sed diam nonumy eirmod tempor invidunt ut labore et dolore magna aliquyam erat, sed diam voluptua. At vero eos et accusam et justo duo dolores et ea rebum.</p>
      <div class="price-box"><span class="tab">Massagen</span>
        <div class="row"><span class="name">Beratungsgespräch Sugaring + Nuvella</span><span class="time"><svg class="ico"><use href="#clock"/></svg>15 min.</span><span class="price"><span class="eur">€</span>49,00</span></div>
        <div class="row"><span class="name">Unterschenkel inkl. Knie</span><span class="time"><svg class="ico"><use href="#clock"/></svg>30 min.</span><span class="price"><span class="eur">€</span>49,00</span></div>
        <div class="row"><span class="name">Beine komplett</span><span class="time"><svg class="ico"><use href="#clock"/></svg>60 min.</span><span class="price"><span class="eur">€</span>95,00</span></div>
        <div class="row"><span class="name">Arme komplett</span><span class="time"><svg class="ico"><use href="#clock"/></svg>30 min.</span><span class="price"><span class="eur">€</span>45,00</span></div>
        <div class="row"><span class="name">Achseln</span><span class="time"><svg class="ico"><use href="#clock"/></svg>15 min.</span><span class="price"><span class="eur">€</span>34,00</span></div>
        <div class="row"><span class="name">Teile Gesicht</span><span class="time"><svg class="ico"><use href="#clock"/></svg>10 min.</span><span class="price"><span class="eur">€</span>15,00</span></div>
      </div>
    </div>
  </div>
</section>

<!-- Men's flyer front -->
<section class="sheet men front theme-cyan">
  <div class="top-bar"></div>
  <div class="photo" role="img" aria-label="Foto: Mann mit Bart, Hand an der Wange" style="left:0;top:150px;width:409px;height:500px;background:linear-gradient(160deg,#e4e4e4,#c9a796 45%,#a57f6c 70%,#d8d6d6)"></div>
  <svg class="wave" style="top:140px" viewBox="0 0 409 60" height="60" preserveAspectRatio="none"><path d="M0 0V32C60 8 110 8 170 22 230 36 240 4 290 6 340 8 370 34 409 28V0Z" fill="#fff"/><path d="M0 32C60 8 110 8 170 22 230 36 240 4 290 6 340 8 370 34 409 28" fill="none" stroke="#5d5d5d" stroke-width="5"/></svg>
  <div class="men-brand"><div class="wordmark">Lumera</div><div class="tagline">Studio für Kosmetik und Pflege</div></div>
  <div class="men-band">
    <svg class="wave" style="top:-40px" viewBox="0 0 409 50" height="50" preserveAspectRatio="none"><path d="M0 50V40C70 40 120 36 170 20 220 4 260 8 300 20 340 32 380 38 409 38V50Z" fill="var(--taupe)"/></svg>
    <h2>ANGEBOTE</h2>
    <div class="sub"><i></i>für Männer<i></i></div>
    <span class="url-pill">www.lumera-studio.de</span>
  </div>
  <div class="badge" style="left:234px;top:495px;width:136px;height:136px;padding-top:12px;font-size:14px;line-height:1.2">
    <svg width="26" height="26" style="color:#fff"><use href="#phone"/></svg>
    <div style="margin-top:6px">TERMINE:</div>
    <div style="font-size:21px;letter-spacing:.01em;line-height:1.1">04120 55<br>38 210</div>
  </div>
</section>

<!-- Men's flyer back -->
<section class="sheet men back theme-cyan">
  <div class="top-bar"></div>
  <div class="men-back-body">
    <h1>Angebote für Männer</h1>
    <p class="intro">Lorem ipsum dolor sit amet, consetetur sadipscing elitr, sed diam nonumy eirmod tempor invidunt ut labore et dolore magna aliquyam erat, sed lios diam voluptua. At vero eos et accusam et justo duo dolores et ea rebum. Lorem ipsum dolor sit amet, consetetur sadipscing elitr, sed diam nonumy eirmod tempor</p>
    <div class="price-box"><span class="tab">Kosmetikbehandlungen</span>
      <div class="row"><span class="name">Lorem ipsum dolor</span><span class="time"><svg class="ico"><use href="#clock"/></svg>90 min.</span><span class="price"><span class="eur">€</span>190,00</span></div>
      <div class="row"><span class="name">Lorem ipsum dolor</span><span class="time"><svg class="ico"><use href="#clock"/></svg>90 min.</span><span class="price"><span class="eur">€</span>280,00</span></div>
      <div class="row"><span class="name">Lorem ipsum dolor</span><span class="time"><svg class="ico"><use href="#clock"/></svg>45 min.</span><span class="price"><span class="eur">€</span>45,00</span></div>
      <div class="row"><span class="name">Lorem ipsum dolor</span><span class="time"><svg class="ico"><use href="#clock"/></svg>60 min.</span><span class="price"><span class="eur">€</span>52,00</span></div>
    </div>
    <div class="price-box"><span class="tab">Massagen</span>
      <div class="row"><span class="name">Lorem ipsum dolor</span><span class="time"><svg class="ico"><use href="#clock"/></svg>90 min.</span><span class="price"><span class="eur">€</span>190,00</span></div>
      <div class="row"><span class="name">Lorem ipsum dolor</span><span class="time"><svg class="ico"><use href="#clock"/></svg>90 min.</span><span class="price"><span class="eur">€</span>280,00</span></div>
      <div class="row"><span class="name">Lorem ipsum dolor</span><span class="time"><svg class="ico"><use href="#clock"/></svg>45 min.</span><span class="price"><span class="eur">€</span>45,00</span></div>
      <div class="row"><span class="name">Lorem ipsum dolor</span><span class="time"><svg class="ico"><use href="#clock"/></svg>60 min.</span><span class="price"><span class="eur">€</span>52,00</span></div>
    </div>
    <div class="price-box"><span class="tab">Maniküre</span>
      <div class="row"><span class="name">Lorem ipsum dolor</span><span class="time"><svg class="ico"><use href="#clock"/></svg>90 min.</span><span class="price"><span class="eur">€</span>190,00</span></div>
      <div class="row"><span class="name">Lorem ipsum dolor</span><span class="time"><svg class="ico"><use href="#clock"/></svg>90 min.</span><span class="price"><span class="eur">€</span>280,00</span></div>
    </div>
    <div class="price-box"><span class="tab">Fußpflege</span>
      <div class="row"><span class="name">Lorem ipsum dolor</span><span class="time"><svg class="ico"><use href="#clock"/></svg>90 min.</span><span class="price"><span class="eur">€</span>190,00</span></div>
      <div class="row"><span class="name">Lorem ipsum dolor</span><span class="time"><svg class="ico"><use href="#clock"/></svg>90 min.</span><span class="price"><span class="eur">€</span>280,00</span></div>
      <div class="row"><span class="name">Lorem ipsum dolor</span><span class="time"><svg class="ico"><use href="#clock"/></svg>45 min.</span><span class="price"><span class="eur">€</span>45,00</span></div>
      <div class="row"><span class="name">Lorem ipsum dolor</span><span class="time"><svg class="ico"><use href="#clock"/></svg>60 min.</span><span class="price"><span class="eur">€</span>52,00</span></div>
      <div class="row"><span class="name">Lorem ipsum dolor</span><span class="time"><svg class="ico"><use href="#clock"/></svg>45 min.</span><span class="price"><span class="eur">€</span>45,00</span></div>
    </div>
  </div>
  <div style="position:absolute;left:38px;bottom:118px"><span class="url-pill" style="font-size:13px;line-height:22px;border-radius:11px">www.lumera-studio.de</span></div>
  <div class="men-contact">
    <h4>Kontakt</h4>
    <div class="line"><svg width="9" height="9" style="color:#fff"><use href="#pin"/></svg>Lindenweg 14 | 20457 Hafenstadt</div>
    <div class="line"><svg width="9" height="9" style="color:#fff"><use href="#phone"/></svg><b>Telefon:</b>04120 55 38 210</div>
    <div class="line"><svg width="9" height="9" style="color:#fff"><use href="#mail"/></svg><b>E-Mail:</b>info@lumera-studio.de</div>
  </div>
  <div class="badge" style="left:256px;top:672px;width:112px;height:112px;padding-top:12px;font-size:13px;line-height:1.45">
    <svg width="24" height="24" style="color:#fff"><use href="#calendar"/></svg>TERMINE<br>ONLINE<br>BUCHEN!
  </div>
</section>

</body>
</html>
```